Wholesale e-commerce website re-design

We are a wholesaler of African-made and African-themed products, and we're looking to update the look and feel of our website www.lomatrade.com to improve user experience. We'd like to have a cleaner homepage that keeps the product category menus (but simplifies them), allows certain products to be featured, and has a simple CTA box (something like "Login" for existing wholesale customers or "Start a Business" for new customers). The layout might be something along the lines of http://www.pinewellmarket.com/ except with a shopping cart featured at the top right. Our colors tend to be earth-toned, but the current color palate looks dated. Also see our blog.lomatrade.com page for themes and color ideas that are maybe more up-to-date. On our product pages, we want to feature the products more prominently and have simpler, cleaner Buy or Add buttons.

Other reference sites for inspiration: dravensupply.com, kettlorhome.com, http://www.pinewellmarket.com, http://morvanbulkgoods.com/ http://tenubra.com/
Updates

Project Deadline Extended
Reason: We like many of the designs that have been submitted so far, but need more time to make our final choice.

Target Market(s)

Small wholesale customers, most have a small business or home-based business. Also some retail, so an option for retail customers to click at the top to see retail pricing would be nice

Industry/Entity Type

Wholesale

Number of Pages Required

3 page

Font styles to use
Sans Serif

Requirements
Must have
• Clean, clear design that highlights products and reduces friction to customer purchase. Should include one homepage, one product page, and one shopping cart page design. Works with all browser types and be mobile-friendly.
Nice to have
• Other color schemes that would look good with our logo (maybe different from colors chosen below).
Should not have
• Splash pages with special effects, Adobe flash, elements that slow down page load times or that only work well in certain browsers.

```html
<!DOCTYPE html>
<html lang="en">
<head>
<meta charset="utf-8">
<title>Loma Trade – Wholesale African Goods</title>
<link rel="stylesheet" href="https://fonts.googleapis.com/css2?family=Lato:ital,wght@0,400;0,700;1,400&display=swap">
<style>
:root{
  --brown:#6b4226;
  --brown-dark:#4a2d18;
  --brown-btn:#6a4a30;
  --red:#c0392b;
  --red-text:#c23b2a;
  --ink:#2b2b2b;
  --muted:#8a8a8a;
  --rule:#a8886e;
  --bar:#2e2a28;
  --white:#ffffff;
}
*{box-sizing:border-box;margin:0;padding:0}
html,body{width:1200px;height:2273px;overflow:hidden;background:var(--white)}
body{font-family:'Lato',sans-serif;color:var(--ink);position:relative}
a{color:inherit;text-decoration:none}
ul{list-style:none}

/* Header */
.brand{position:absolute;left:238px;top:30px;display:flex;align-items:center;gap:8px}
.brand-mark{width:16px;height:16px;background:var(--red)}
.brand-name{font-weight:700;font-size:17px;letter-spacing:1px;color:var(--ink)}
.social{position:absolute;left:505px;top:14px;display:flex;gap:8px}
.social span{width:25px;height:25px;border-radius:50%;background:#8d8d8d;display:block}
.account{position:absolute;left:760px;top:14px;display:flex;gap:9px}
.account a{background:var(--brown-btn);color:var(--white);font-size:12px;height:27px;border-radius:3px;display:flex;align-items:center;gap:10px;padding:0 14px 0 10px}
.account a.signup{width:96px}
.account a.login{width:99px;padding-left:14px}
.account svg{width:13px;height:14px}
.search{position:absolute;left:532px;top:71px;display:flex}
.search input{width:115px;height:20px;border:1px solid #9a9a9a;font:italic 10px 'Lato',sans-serif;padding:0 6px;color:#999}
.search button{width:20px;height:20px;background:#9a9a9a;border:0;display:flex;align-items:center;justify-content:center}
.cart{position:absolute;left:834px;top:67px;display:flex;gap:6px;align-items:center}
.cart svg{width:28px;height:24px}
.cart strong{display:block;color:var(--red);font-size:12px;font-weight:400;line-height:12px}
.cart small{display:block;color:var(--muted);font-size:10px;line-height:11px}
.nav{position:absolute;left:253px;top:108px;display:flex;font-size:12px;letter-spacing:.3px}
.nav a{margin-right:26px}
.nav a:last-child{margin-right:0}

/* Hero */
.hero{position:absolute;left:0;top:138px;width:1200px;height:389px;background:linear-gradient(180deg,#f4e3b2 0%,#e8c58e 32%,#e3ad6a 60%,#dba266 100%)}
.hero-copy{position:absolute;left:0;top:230px;width:1200px;text-align:center;color:#3b2b20}
.hero-copy h1{font-weight:400;font-size:35px;letter-spacing:3px;line-height:40px}
.hero-copy h1 b{display:block;font-weight:700;font-size:46px;letter-spacing:5px;line-height:54px}
.hero-copy p{margin-top:18px;font-size:17px;color:var(--red-text);letter-spacing:.5px}
.hero-cta{display:inline-block;margin-top:19px;width:136px;height:40px;line-height:38px;border:1.5px solid var(--red-text);border-radius:3px;color:var(--red-text);font-size:17px}

/* Featured */
.section-title{position:absolute;left:240px;width:720px;top:600px;display:flex;align-items:center;gap:12px;color:var(--brown);font-size:22px;letter-spacing:1px}
.section-title::before,.section-title::after{content:"";flex:1;height:1px;background:var(--rule)}
.arrow{position:absolute;top:795px;width:16px;height:30px}
.arrow.prev{left:148px}.arrow.next{left:1033px}
.products{position:absolute;left:240px;top:690px;display:flex}
.product{width:150px;margin-right:42px}
.product:last-child{margin-right:0}
.product .photo{height:128px;border-radius:4px}
.product h3{margin-top:10px;font-size:12px;color:var(--red-text);font-weight:700}
.product p{margin-top:6px;font-size:13px;line-height:19.5px}
.product .price{margin-top:6px;color:var(--red-text);font-size:13px;font-weight:700}

/* Promises */
.promises{position:absolute;left:240px;top:993px;width:720px;height:296px;display:flex}
.promise{width:360px;height:296px;color:var(--white);text-align:center;padding:66px 22px 0}
.promise.shipping{background:linear-gradient(135deg,#9a6a44,#7a4e2e 60%,#6a4127)}
.promise.guarantee{background:linear-gradient(135deg,#8a6a50,#6e5038 60%,#5d412c)}
.promise h2{font-weight:400;font-size:22px;letter-spacing:.5px}
.promise p{margin-top:14px;font-size:11.5px;line-height:18px}

/* Blog & upload */
.col-title{position:absolute;top:1355px;font-size:22px;color:var(--brown);letter-spacing:.5px}
.blog{position:absolute;left:240px;top:1412px;width:342px}
.post{padding-bottom:14px;border-bottom:1px solid #c9c9c9;margin-bottom:14px}
.post:last-child{border:0}
.post h3{font-size:12px;color:var(--red-text);font-weight:700}
.post time{display:block;margin-top:4px;font-size:11.5px;font-style:italic;color:var(--muted)}
.post p{margin-top:8px;font-size:12px;line-height:19px}
.post p b{font-weight:700}
.video{position:absolute;left:617px;top:1416px;width:343px;height:191px;background:linear-gradient(180deg,#cfcfcf 0%,#8f8f8f 45%,#3c3c3c 100%)}
.video .controls{position:absolute;left:0;bottom:0;width:100%;height:22px;background:#111;color:#ccc;font-size:8px;display:flex;align-items:center;padding:0 6px;gap:6px}
.video .controls::before{content:"";position:absolute;left:0;top:0;width:100%;height:2px;background:#777}
.newsletter{position:absolute;left:618px;top:1676px;width:315px;font-size:17px;line-height:25px;color:var(--red-text)}
.subscribe{position:absolute;left:618px;top:1757px;display:flex;gap:10px}
.subscribe input{width:222px;height:29px;border:1px solid #aaa;border-radius:3px;font:12px 'Lato',sans-serif;padding:0 8px;color:#999}
.subscribe button{width:111px;height:29px;background:var(--red);color:#fff;border:0;border-radius:3px;font:700 12px 'Lato',sans-serif}

/* Footer */
.footer{position:absolute;left:0;top:1880px;width:1200px;height:342px;background:linear-gradient(90deg,#a8794f 0%,#8a5a35 45%,#7b4d2b 100%)}
.footer-col{position:absolute;top:72px;color:var(--white)}
.footer-col h4{font-weight:400;font-size:17px;padding-bottom:5px;border-bottom:1px solid rgba(255,255,255,.75);width:148px}
.footer-col ul{margin-top:12px}
.footer-col li{font-size:11.5px;line-height:18px;padding-left:13px;position:relative}
.footer-col li::before{content:"";position:absolute;left:0;top:5px;border-left:7px solid #fff;border-top:4px solid transparent;border-bottom:4px solid transparent}
.footer-col.contact li{padding-left:0}
.footer-col.contact li::before{display:none}
.footer-col.contact .gap{height:18px}
.copyright{position:absolute;left:0;top:2222px;width:1200px;height:51px;background:var(--bar);color:#fff;font-size:11.5px;text-align:center;line-height:51px}
</style>
</head>
<body>

<header>
  <a class="brand" href="#"><span class="brand-mark"></span><span class="brand-name">LOMA TRADE</span></a>
  <div class="social" aria-label="Social links">
    <span></span><span></span><span></span><span></span><span></span><span></span>
  </div>
  <div class="account">
    <a class="signup" href="#"><svg viewBox="0 0 13 14"><circle cx="6.5" cy="4" r="3" fill="#fff"/><path d="M1 14c0-4 2.5-6 5.5-6s5.5 2 5.5 6z" fill="#fff"/></svg>Sign up</a>
    <a class="login" href="#"><svg viewBox="0 0 13 14"><rect x="1" y="6" width="11" height="8" rx="1" fill="#fff"/><path d="M3.5 6V4a3 3 0 0 1 6 0v2" fill="none" stroke="#fff" stroke-width="1.8"/></svg>Login</a>
  </div>
  <form class="search"><input type="text" placeholder="Search"><button type="button" aria-label="Search"><svg width="11" height="11" viewBox="0 0 11 11"><circle cx="4.5" cy="4.5" r="3.3" fill="none" stroke="#fff" stroke-width="1.5"/><path d="M7 7l3.3 3.3" stroke="#fff" stroke-width="1.6"/></svg></button></form>
  <a class="cart" href="#"><svg viewBox="0 0 28 24"><path d="M1 2h4l3 13h15l3-9H7" fill="none" stroke="#c0392b" stroke-width="2.4"/><path d="M7 6h19l-3 9H9z" fill="#c0392b"/><circle cx="10" cy="20" r="2.2" fill="#c0392b"/><circle cx="21" cy="20" r="2.2" fill="#c0392b"/></svg><span><strong>Shopping Cart</strong><small>0 items in your cart</small></span></a>
  <nav class="nav">
    <a href="#">CLOTHING</a><a href="#">FABRICS</a><a href="#">HEALTH &amp; BEAUTY</a><a href="#">JEWELRY</a><a href="#">INSTRUMENTS</a><a href="#">ARTWORK</a><a href="#">MISCELLANEOUS</a>
  </nav>
</header>

<section class="hero" role="img" aria-label="Sunlit desert plain with distant mountains"></section>
<div class="hero-copy">
  <h1>HOW TO START YOUR OWN<b>AFRICAN BUSINESS</b></h1>
  <p>Complete success step-by-step</p>
  <a class="hero-cta" href="#">Get started</a>
</div>

<h2 class="section-title">FEATURED PRODUCTS</h2>
<svg class="arrow prev" viewBox="0 0 16 30"><path d="M13 3L3 15l10 12" fill="none" stroke="#222" stroke-width="3"/></svg>
<svg class="arrow next" viewBox="0 0 16 30"><path d="M3 3l10 12L3 27" fill="none" stroke="#222" stroke-width="3"/></svg>
<div class="products">
  <article class="product">
    <div class="photo" role="img" aria-label="Two tie-dye heart kaftans with matching head scarves" style="background:linear-gradient(90deg,#f2c14a,#e58a3a 45%,#b46fb0 60%,#f0f0f0)"></div>
    <h3>Tie-Dye Heart Kaftan</h3>
    <p>Fits up to 62" bust. 57" length. Matching head scarf. 100% cotton.</p>
    <div class="price">$11.95</div>
  </article>
  <article class="product">
    <div class="photo" role="img" aria-label="Two mud cloth dresses in dark and cream prints" style="background:linear-gradient(90deg,#f4f4f4,#4a5866 35%,#d9cfa8 70%,#f4f4f4)"></div>
    <h3>Mud Cloth Dress</h3>
    <p>Fits up to a 44" bust and 53" length. Sleeve length can vary.</p>
    <div class="price">$29.95</div>
  </article>
  <article class="product">
    <div class="photo" role="img" aria-label="Bar of shea butter soap beside its yellow box" style="background:linear-gradient(180deg,#f6f6f6,#f0e35a 45%,#e0c88a 75%,#f6f6f6)"></div>
    <h3>Raw Shea Butter Soap</h3>
    <p>Raw Shea moisturizes, aloe heals and vitamin E strengthens your skin.</p>
    <div class="price">$1.99</div>
  </article>
  <article class="product">
    <div class="photo" role="img" aria-label="Three children's dashiki and shorts sets" style="background:linear-gradient(90deg,#f5f5f5,#3c8a4a 30%,#d8443a 55%,#e6b23a 75%,#f5f5f5)"></div>
    <h3>Children Dashiki &amp; Shorts</h3>
    <p>Comes with dashiki and shorts. Comes in 3 sizes: Small, Medium, and Large.</p>
    <div class="price">$11.95</div>
  </article>
</div>

<section class="promises">
  <div class="promise shipping" role="img" aria-label="Warm-toned photo of a packing desk behind the shipping notice">
    <h2>SAME DAY SHIPPING</h2>
    <p>Order before 2 PM (EST) to ship your order today! (US Mail orders will be shipped the same day before 11:30 AM). Especially large orders placed after noon may be sent on the following day. No shipments are sent on Saturday, Sunday, or holidays. Orders can not be changed or added to on the day they are being shipped.</p>
  </div>
  <div class="promise guarantee" role="img" aria-label="Warm-toned photo of a handshake behind the guarantee notice">
    <h2>100% GUARANTEE</h2>
    <p>You are guaranteed to be 100% satisfied with anything that you order. If you are not happy for any reason at all (or even no reason at all), you can return it for your choice of either a full refund or exchange. All returns must be undamaged and returned within 30 days of your purchase. We do not pay shipping costs for returns.</p>
  </div>
</section>

<h2 class="col-title" style="left:240px">LATEST BLOG</h2>
<h2 class="col-title" style="left:617px">NEWEST UPLOAD</h2>

<div class="blog">
  <article class="post">
    <h3>New Hand-Carved Ebony Artwork Just in Time for Christmas!</h3>
    <time>December 8, 2016</time>
    <p>Are you looking for a stunning piece of hand-crafted artwork as a christmas gift? We've gotten a huge shipment of intricately crafted ebony art pieces anyone will love. But before we get to the items, what makes ebony so special? <b>Read More &gt;&gt;</b></p>
  </article>
  <article class="post">
    <h3>Discover the History of the Maasai Sword</h3>
    <time>December 1, 2016</time>
    <p>We're so excited to present this African Maasai sword from Kenya. They are the constant side arm of the Maasai warrior. The sword is light and short, with a double-edged, leaf-shaped spatula blade made from steel. <b>Read More &gt;&gt;</b></p>
  </article>
  <article class="post">
    <h3>The History and Meaning of the Zulu Shield</h3>
    <time>November 11, 2016</time>
    <p>We're thrilled and excited to add the historic Zulu shields to our collection of African weaponry this season! What makes these shields so special? They have been a part of African history for centuries and were used by Zulu tribesmen. <b>Read More &gt;&gt;</b></p>
  </article>
</div>

<div class="video" role="img" aria-label="Video still of a snowy mountain landscape">
  <div class="controls"><span>▶</span><span>▶|</span><span>3:24 / 3:26</span></div>
</div>

<p class="newsletter">Sign up to our newsletter for a 6-email lesson on how to get more customers.</p>
<form class="subscribe"><input type="email" placeholder="email1234@hello.com"><button type="button">Subscribe</button></form>

<footer class="footer" role="img" aria-label="Warm brown-toned photo of smiling customers">
  <div class="footer-col" style="left:240px">
    <h4>Business Tools</h4>
    <ul>
      <li>Free Printable Products</li><li>Get Your Own Website</li><li>Fast Start-Up Kit</li><li>How To Start A Business</li><li>Promotional Tools</li><li>Affiliate Program</li><li>Free Business Tips</li><li>How to Buy for Business</li><li>More Free Business Help</li>
    </ul>
  </div>
  <div class="footer-col" style="left:427px">
    <h4>Customer Help</h4>
    <ul>
      <li>Catalogs</li><li>African Stores Near You</li><li>FAQ</li><li>Shipping Policies</li><li>See Retail Pricing</li><li>International Policies</li><li>Check Your Order Status</li><li>Returns</li><li>Privacy Policy</li>
    </ul>
  </div>
  <div class="footer-col" style="left:616px">
    <h4>About Imports</h4>
    <ul>
      <li>About Loma Trade</li><li>How We Help Africa</li><li>African Proverbs</li><li>Free Articles</li><li>How Can We Improve?</li><li>African Groups</li><li>African cultural tradition</li><li>African Recipes</li><li>2016 African Calendar</li>
    </ul>
  </div>
  <div class="footer-col contact" style="left:795px">
    <h4>Contact Us</h4>
    <ul>
      <li>Tel: (201) 555-0148</li><li>Fax: (866) 555-0172</li><li>contact@lomatrade.com</li><li>118 Cedar Lane, Unit B</li><li>Fairbrook, NJ 07090</li>
      <li class="gap"></li>
      <li>9 AM to 7 PM EST on Mon-Fri</li><li>9 AM to 3 PM EST on Saturday</li><li>Toll Free: (800) 555-0190</li>
    </ul>
  </div>
</footer>
<div class="copyright">©1998-2016 Loma Trade. All rights reserved.</div>

</body>
</html>
```